Book Cover Design Project

Hello,

I am looking to get a cover created for my book.

Size 6 X 9

Title:
Quiet Ledger Steady Gains

Sub-Title:
Plain Methods for Growing Steady Gains Within Your Quiet Ledger

Author:
Martin Fenwick

The book could have an image or only typography.

If it does include an image do not use an image of a real person. If you use a person, he can be shaded in, outlined, etc

I like the color white and blue however, I am open to other colors as well.

Below is the cover of my previous book that has an image:
http://www.quillmarket.example/Dawn-Of-Stag-Path-Vowed-Final/dp/284610375K/ref=sr_1_1?ie=UTF8&s=books&qid=2417307529&sr=1-1

I like simple designs but open to other concepts also

attached is the text to be used for the back of the book.

Thank you in advance for your designs,

Target Market(s)

This book will be for small business owners. Typically males/females between the age of 25 - 45 looking to make more money without going broke with marketing.

Industry/Entity Type

Business

Requirements
Must have
• Must include the Title, Subtitle and Author on the cover

Nice to have
• An image that represents a small business growing
Should not have
• Images of a real person. Stylized versions are ok.

```html
<!DOCTYPE html>
<html lang="en">
<head>
<meta charset="utf-8">
<title>Quiet Ledger Steady Gains – Book Cover</title>
<link rel="stylesheet" href="https://fonts.googleapis.com/css2?family=Open+Sans:wght@700&family=Fira+Sans+Condensed:wght@600;700&family=Tinos:ital,wght@0,700;1,700&display=swap">
<style>
  :root {
    --sky-top: #0c55cc;
    --sky-bottom: #2198e6;
    --spine: #0a47bd;
    --white: #ffffff;
    --yellow: #ffe81a;
    --grid: rgba(255,255,255,0.85);
    --glow: rgba(10,40,140,0.7);
  }
  html, body { margin: 0; padding: 0; overflow: hidden; }
  body { width: 1200px; height: 882px; }
  .cover {
    position: relative;
    width: 1200px; height: 882px;
    background: linear-gradient(180deg, var(--sky-top) 0%, var(--sky-bottom) 100%);
    overflow: hidden;
    color: var(--white);
  }
  .spine {
    position: absolute; left: 588px; top: 0; width: 26px; height: 882px;
    background: var(--spine);
  }
  /* Back cover */
  .back {
    position: absolute; left: 63px; top: 76px; width: 486px;
    font-family: "Open Sans", sans-serif; font-weight: 700;
    font-size: 14.5px; line-height: 19.5px; letter-spacing: 0.35px;
  }
  .back p { margin: 0 0 19px; text-align: justify; }
  .back .headline {
    color: var(--yellow); font-size: 21.5px; line-height: 25px; letter-spacing: 0.3px;
    text-align: left; margin-bottom: 17px;
  }
  .back .offer { margin-left: 4px; }
  .benefits { list-style: none; margin: 0 0 19px; padding: 0; color: var(--yellow); }
  .benefits li::before { content: "\2022\00a0"; }
  .about-title { margin-top: 36px !important; }
  .link { color: var(--yellow); }
  /* Front cover */
  .author {
    position: absolute; left: 614px; width: 586px; top: 64px;
    text-align: center; font-family: "Tinos", serif; font-weight: 700;
    font-size: 27px; letter-spacing: 13px;
  }
  .chart { position: absolute; left: 614px; top: 120px; }
  .contrail {
    position: absolute; left: 480px; top: 381px; width: 642px; height: 7px;
    transform: rotate(-18deg); transform-origin: left center;
    background: linear-gradient(90deg, rgba(255,255,255,0) 0%, rgba(255,255,255,0.45) 40%, rgba(255,255,255,0.95) 100%);
    border-radius: 4px;
  }
  .title {
    position: absolute; left: 614px; width: 586px; text-align: center;
    font-family: "Fira Sans Condensed", sans-serif;
    text-shadow: 0 0 10px var(--glow), 0 0 3px var(--glow);
    white-space: nowrap;
  }
  .title-top { top: 458px; font-size: 64px; font-weight: 600; color: var(--white); letter-spacing: -1px; }
  .title-main { top: 530px; font-size: 90px; font-weight: 700; color: var(--yellow); letter-spacing: -2px; line-height: 1.1; }
  .subtitle {
    position: absolute; left: 614px; width: 586px; top: 670px;
    text-align: center; font-family: "Tinos", serif; font-style: italic; font-weight: 700;
    font-size: 34px; line-height: 51px;
    text-shadow: 2px 2px 3px var(--glow);
  }
</style>
</head>
<body>
<div class="cover">
  <section class="back">
    <p class="headline">"Dramatically Increase Your Sales And<br>Revenue With Effective Marketing<br>Strategies, Guaranteed To Get Results!"</p>
    <p>Are lackluster sales getting you down?</p>
    <p>Does it seem like -- no matter how much testing and tweaking you do -- you continue to struggle with getting new customers, creating a strong online and offline presence, and maximizing the lifetime value of existing customers, and now you're running out of time, patience... and money?</p>
    <p class="offer">What if I told you that I could help you:</p>
    <ul class="benefits">
      <li>Gain and retain new customers</li>
      <li>Get others to promote your business</li>
      <li>Make more money from your existing customers</li>
      <li>Get results that will blow your competition away</li>
    </ul>
    <p>... And I can show you how to do it FASTER, for a small fraction of what you'd pay in-house marketing employees to get the SAME results!</p>
    <p>Curious? Then open this book right now and I'll explain how it's done...</p>
    <p class="about-title">About the Author:</p>
    <p>Martin Fenwick is a partner of Brightlane Marketing, which helps small businesses get more customers by making them findable on the Internet. He is a best selling author and has a bachelor's degree in Internet Marketing. He dedicates his time to learning as much as possible, both in marketing and in life.</p>
    <p>See how he can serve your business by going to<br><span class="link">www.brightlanemarketing.example</span></p>
  </section>

  <div class="spine"></div>

  <div class="author">Martin Fenwick</div>

  <svg class="chart" width="586" height="290" viewBox="0 0 586 290" aria-label="Revenue growth chart 2006 to 2012">
    <g stroke="var(--grid)" stroke-width="1.5" fill="none">
      <line x1="34" y1="12" x2="533" y2="12"/>
      <line x1="34" y1="43" x2="533" y2="43"/>
      <line x1="34" y1="74" x2="533" y2="74"/>
      <line x1="34" y1="106" x2="533" y2="106"/>
      <line x1="34" y1="137" x2="533" y2="137"/>
      <line x1="34" y1="168" x2="533" y2="168"/>
      <line x1="34" y1="199" x2="533" y2="199"/>
      <line x1="34" y1="230" x2="533" y2="230"/>
      <line x1="86" y1="261" x2="533" y2="261"/>
      <line x1="533" y1="12" x2="533" y2="261"/>
      <line x1="86" y1="255" x2="86" y2="267"/>
      <line x1="157" y1="255" x2="157" y2="267"/>
      <line x1="220" y1="255" x2="220" y2="267"/>
      <line x1="283" y1="255" x2="283" y2="267"/>
      <line x1="346" y1="255" x2="346" y2="267"/>
      <line x1="409" y1="255" x2="409" y2="267"/>
      <line x1="472" y1="255" x2="472" y2="267"/>
    </g>
    <g fill="var(--white)" font-family="Open Sans, sans-serif" font-weight="700" font-size="12.5">
      <text x="38" y="35">$ 155K</text>
      <text x="38" y="66">$ 139K</text>
      <text x="38" y="98">$ 125K</text>
      <text x="38" y="129">$ 111K</text>
      <text x="38" y="160">$ 95K</text>
      <text x="38" y="191">$ 95K</text>
      <text x="38" y="222">$ 70K</text>
      <text x="44" y="253">$ 50K</text>
    </g>
    <g fill="var(--white)" font-family="Open Sans, sans-serif" font-weight="700" font-size="12.5" text-anchor="middle">
      <text x="124" y="279">2006</text>
      <text x="188" y="279">2007</text>
      <text x="251" y="279">2008</text>
      <text x="314" y="279">2009</text>
      <text x="377" y="279">2010</text>
      <text x="440" y="279">2011</text>
      <text x="503" y="279">2012</text>
    </g>
  </svg>
  <div class="contrail" role="img" aria-label="Jet airplane with white contrail climbing across the chart"></div>

  <div class="title title-top">Quiet Ledger</div>
  <div class="title title-main">STEADY GAINS</div>
  <div class="subtitle">Plain Methods for Growing<br>Steady Gains Within Your<br>Quiet Ledger</div>
</div>
</body>
</html>
```